Design a book cover for a presidential candidate

Design a print and e-book cover from the attached materials. We want a patriotic nonpartisan cover for an independent candidate in the 2016 Presidential race. The design should be somewhat futuristic, technologically advanced, and yet communicate fairness and balance. The Title, subtitles, back cover copy and quotes are all in the attached material. Use any of the photos attached.

```html
<!DOCTYPE html>
<html lang="en">
<head>
<meta charset="utf-8">
<title>Grant Ellison – Independent Candidate</title>
<link rel="stylesheet" href="https://fonts.googleapis.com/css2?family=Archivo+Narrow:wght@700&family=Arimo:wght@700&display=swap">
<style>
  :root {
    --blue: #00a9e8;
    --blue-light: #1bbde6;
    --blue-deep: #0b79c2;
    --red: #c8202f;
    --white: #ffffff;
    --ink: #232323;
    --sepia-light: #c99a4a;
    --sepia-mid: #8a5f22;
    --sepia-dark: #3a2508;
  }
  html, body { margin: 0; padding: 0; overflow: hidden; background: var(--white); }
  .cover {
    position: relative;
    width: 1200px; height: 780px;
    background: var(--white);
    overflow: hidden;
  }
  .block { position: absolute; }
  .band-top { left: 0; top: 0; width: 1200px; height: 98px; background: var(--blue); }
  .band-top-corner { left: 1080px; top: 0; width: 120px; height: 98px; background: linear-gradient(to top left, var(--blue-deep) 50%, transparent 50%); }
  .band-top-bar { left: 0; top: 40px; width: 622px; height: 30px; background: var(--white); }
  .band-top-line { left: 0; top: 50px; width: 410px; height: 8px; background: var(--red); }
  .edge-left { left: 0; top: 98px; width: 8px; height: 682px; background: var(--blue); }
  .edge-right { left: 1188px; top: 98px; width: 12px; height: 480px; background: var(--blue); }
  .pillar-a { left: 622px; top: 98px; width: 18px; height: 667px; background: var(--blue); }
  .pillar-b { left: 682px; top: 98px; width: 33px; height: 667px; background: var(--blue); }
  .rule-mid { left: 0; top: 574px; width: 1200px; height: 14px; background: var(--blue); }
  .atoms { position: absolute; left: 690px; top: 4px; }

  .quotes {
    position: absolute; left: 8px; top: 100px; width: 568px; height: 474px;
    display: flex; align-items: center; justify-content: center;
    padding-top: 56px; box-sizing: border-box;
  }
  .quotes p {
    margin: 0; text-align: center; white-space: nowrap;
    font-family: "Archivo Narrow", "Arial Narrow", sans-serif;
    font-weight: 700; font-size: 20px; line-height: 29px; color: var(--ink);
  }
  .portrait {
    position: absolute; left: 742px; top: 130px; width: 443px; height: 443px;
    background: radial-gradient(ellipse at 55% 40%, var(--sepia-light) 0%, var(--sepia-mid) 45%, var(--sepia-dark) 100%);
  }
  .title-box {
    position: absolute; top: 588px; height: 177px;
    background: var(--blue-light);
    color: var(--white);
    font-family: "Arimo", Arial, sans-serif; font-weight: 700;
    text-align: center;
    text-shadow: 0 2px 3px rgba(0,0,0,.25);
  }
  .title-box .underline {
    position: absolute; top: 144px; height: 14px;
    background: linear-gradient(var(--red) 0 5px, var(--white) 5px 9px, var(--red) 9px 14px);
  }
  .title-left { left: 20px; width: 575px; }
  .title-left .subtitle { margin: 44px 0 0; font-size: 30px; line-height: 37px; }
  .title-left .underline { left: 88px; width: 434px; }
  .title-right { left: 715px; width: 480px; box-shadow: 0 4px 10px rgba(0,0,0,.35); }
  .title-right .book-title { margin: 22px 0 0; font-size: 40px; line-height: 46px; letter-spacing: 1px; }
  .title-right .subtitle { margin: 6px 0 0; font-size: 24px; line-height: 30px; }
  .title-right .underline { left: 15px; width: 432px; }
</style>
</head>
<body>
<div class="cover">
  <div class="block band-top"></div>
  <div class="block band-top-corner"></div>
  <div class="block band-top-bar"></div>
  <div class="block band-top-line"></div>
  <div class="block edge-left"></div>
  <div class="block edge-right"></div>
  <div class="block pillar-a"></div>
  <div class="block pillar-b"></div>
  <div class="block rule-mid"></div>

  <svg class="atoms" width="350" height="96" viewBox="0 0 350 96" fill="none" stroke="#ffffff" stroke-width="3" aria-hidden="true">
    <g transform="translate(40 48)">
      <ellipse rx="31" ry="11"/><ellipse rx="31" ry="11" transform="rotate(60)"/><ellipse rx="31" ry="11" transform="rotate(-60)"/>
      <circle r="3" fill="#ffffff"/>
    </g>
    <g transform="translate(155 48)">
      <ellipse rx="37" ry="12"/><ellipse rx="37" ry="12" transform="rotate(60)"/><ellipse rx="37" ry="12" transform="rotate(-60)"/>
      <circle r="3" fill="#ffffff"/>
    </g>
    <g transform="translate(290 50)">
      <ellipse rx="42" ry="14"/><ellipse rx="42" ry="14" transform="rotate(60)"/><ellipse rx="42" ry="14" transform="rotate(-60)"/>
      <circle r="3.5" fill="#ffffff"/>
    </g>
  </svg>

  <section class="quotes">
    <p>
      Grant Ellison's analysis of the economy should be required reading for<br>
      every Economics 101 class in the nation.”<br>
      Dale Warner, former Director of Private Equity at Halden Crowe<br>
      In the midst of all the mudslinging and partisan ideology today, Grant's<br>
      balanced approach to the economy is truly a breath of fresh air.” – Maria<br>
      Kessler, Director of Women Building Tech<br>
      This is the type of thinking that could win a Laurel Prize. With solutions so<br>
      insightful and compelling they appeal to both conservatives and liberals,<br>
      Ellison is likely to become a hot topic in the 2016 Presidential race.” —<br>
      Owen Pratt, guerilla-marketing guru
    </p>
  </section>

  <div class="portrait" role="img" aria-label="Sepia portrait photo of the candidate in a leather jacket in front of pine trees"></div>

  <div class="title-box title-left">
    <p class="subtitle">Independent candidate in the<br>2016 Presidential race</p>
    <div class="underline"></div>
  </div>
  <div class="title-box title-right">
    <h1 class="book-title">GRANT ELLISON</h1>
    <p class="subtitle">Independent candidate in the<br>2016 Presidential race</p>
    <div class="underline"></div>
  </div>
</div>
</body>
</html>
```